Brochure for medical doctor

I need a brochure for a medical doctor to promote his practice. The brochure should contain his picture, business information (use letterhead from attachment), and the following text:

- Now accepting PI cases on lien!
- Same and next business day appointments available for initial visits, pre-operative clearances, and all other medical needs

- Expedited medical reports sent quickly to your office

Medical

```html
<!DOCTYPE html>
<html lang="en">
<head>
<meta charset="utf-8">
<title>Willowbrook Medical Center – Brochure</title>
<link rel="stylesheet" href="https://fonts.googleapis.com/css2?family=Montserrat:wght@300;400;500;700&family=Roboto:wght@400&display=swap">
<style>
  :root{
    --blue-deep:#1a4a9c;
    --blue-mid:#0f6fbf;
    --blue-bright:#1396d6;
    --blue-text:#1b8fd0;
    --ink:#111111;
    --grey-band:#e6e6e6;
    --white:#ffffff;
  }
  *{margin:0;padding:0;box-sizing:border-box}
  html,body{width:848px;height:1200px;overflow:hidden;background:var(--white)}
  .brochure{position:relative;width:848px;height:1200px;overflow:hidden;font-family:"Roboto",sans-serif;color:var(--ink)}
  .hero-photo{position:absolute;left:0;top:0;width:848px;height:612px;
    background:linear-gradient(135deg,#c9ced6 0%,#e9ebee 35%,#f4f5f6 55%,#d8dde3 100%)}
  .shapes{position:absolute;left:0;top:0}
  .site-url{position:absolute;left:45px;top:30px;font:700 18px "Montserrat",sans-serif;color:var(--white);letter-spacing:.2px}
  .headline{position:absolute;font-family:"Montserrat",sans-serif;color:var(--white);white-space:nowrap}
  .headline-1{left:211px;top:443px;font-size:21.5px;font-weight:700}
  .headline-1 .amp{font-weight:400}
  .headline-2{left:258px;top:474px;font-size:21.5px;font-weight:700}
  .headline-3{left:140px;top:510px;font-size:40px;font-weight:300;letter-spacing:.5px}
  .tagline{position:absolute;left:54px;top:581px;font:400 19px "Montserrat",sans-serif;color:var(--white)}
  .doctor-portrait{position:absolute;left:659px;top:519px;width:162px;height:162px;border-radius:50%;
    background:linear-gradient(135deg,var(--blue-deep),var(--blue-bright));padding:10px}
  .doctor-portrait .photo{width:100%;height:100%;border-radius:50%;border:2px solid var(--white);
    background:radial-gradient(circle at 50% 45%,#b08a6a 0%,#6e5340 55%,#3b2d24 100%)}
  .divider{position:absolute;left:472px;top:630px;width:376px;height:2px;background:#dcdcdc;z-index:0}
  .doctor-portrait{z-index:1}
  .doctor-name{position:absolute;left:472px;top:645px;font:700 19.5px "Montserrat",sans-serif}
  .doctor-title{position:absolute;left:621px;top:672px;font:400 17px "Montserrat",sans-serif}
  .doctor-bio{position:absolute;left:472px;top:710px;width:336px;font-size:13px;line-height:17.1px}
  .doctor-bio p{margin-bottom:11px}
  .feature{position:absolute;left:68px;display:flex;align-items:flex-start}
  .feature-icon{width:46px;height:46px;flex:none}
  .feature-bar{position:absolute;left:62px;width:5px;background:linear-gradient(var(--blue-bright),var(--blue-deep))}
  .feature-text{position:absolute;left:83px;font-size:16.3px;line-height:20.6px;color:var(--blue-text);white-space:nowrap}
  .feature-pi{top:672px}
  .feature-pi .feature-bar{top:1px;height:40px}
  .feature-pi .feature-text{top:0}
  .feature-appt{top:768px}
  .feature-appt .feature-bar{top:0;height:77px}
  .feature-appt .feature-text{top:-3px}
  .feature-reports{top:896px}
  .feature-reports .feature-bar{top:1px;height:57px}
  .feature-reports .feature-text{top:-1px}
  .brand-name{position:absolute;left:120px;top:1038px;font:500 41px/1.08 "Montserrat",sans-serif;color:var(--ink);letter-spacing:.5px}
  .address{position:absolute;left:120px;top:1160px;font:500 15.5px "Montserrat",sans-serif}
  .call-to-action{position:absolute;left:588px;top:1057px;font:500 18px "Montserrat",sans-serif;color:var(--blue-text)}
  .contact-line{position:absolute;right:40px;font:400 22px "Montserrat",sans-serif;color:var(--white);white-space:nowrap}
  .contact-line .label{font-size:17px;font-weight:300}
  .contact-line .num{font-weight:500}
  .contact-phone{top:1118px}
  .contact-fax{top:1155px}
</style>
</head>
<body>
<div class="brochure">
  <div class="hero-photo" role="img" aria-label="Photo of a physician in a white coat measuring a patient's blood pressure with a cuff"></div>

  <svg class="shapes" width="848" height="1200" viewBox="0 0 848 1200" aria-hidden="true">
    <defs>
      <linearGradient id="bandDeep" x1="0" y1="1" x2="1" y2="0">
        <stop offset="0" stop-color="#1a4a9c"/><stop offset="1" stop-color="#1396d6"/>
      </linearGradient>
      <linearGradient id="bandLight" x1="0" y1="0" x2="1" y2="0">
        <stop offset="0" stop-color="#1396d6"/><stop offset="1" stop-color="#0f6fbf"/>
      </linearGradient>
      <linearGradient id="footerBlue" x1="0" y1="1" x2="1" y2="0">
        <stop offset="0" stop-color="#1a4a9c"/><stop offset="1" stop-color="#1578c8"/>
      </linearGradient>
    </defs>
    <polygon points="396,427 528,355 690,355 619,427" fill="#1a4a9c"/>
    <polygon points="588,458 780,458 848,390 848,198" fill="url(#bandDeep)"/>
    <polygon points="560,548 645,458 610,458 500,548" fill="#e3e3e3"/>
    <polygon points="0,612 62,612 0,675" fill="#e6e6e6"/>
    <polygon points="186,427 619,427 475,570 42,570" fill="url(#bandDeep)"/>
    <polygon points="42,570 475,570 435,612 0,612" fill="url(#bandLight)"/>
    <polygon points="90,1139 532,1139 472,1200 33,1200" fill="var(--grey-band)"/>
    <polygon points="574,1095 848,1095 848,1200 472,1200" fill="url(#footerBlue)"/>
  </svg>

  <div class="site-url">www.willowbrookmedical.com</div>

  <div class="headline headline-1">COMPREHENSIVE <span class="amp">&amp;</span></div>
  <div class="headline headline-2">COMPASSIONATE</div>
  <div class="headline headline-3">MEDICAL CARE</div>
  <div class="tagline">wide range of top-notch health services</div>

  <div class="divider"></div>
  <div class="doctor-portrait"><div class="photo" role="img" aria-label="Portrait photo of Dr. Daniel Marwood"></div></div>
  <div class="doctor-name">Dr. Daniel Marwood</div>
  <div class="doctor-title">MD</div>
  <div class="doctor-bio">
    <p>Dr. Marwood began his medical education as a an undergraduate at the Westbrook State University, where he developed a passion for medicine. He graduated from WSU summa cum laude, and went on to medical school at Harborview University School of Medicine.</p>
    <p>Dr. Marwood completed his residency at Lakeside Community Medical Center in Fairhaven, California.</p>
    <p>At Willowbrook Medical Center, Dr. Marwood addresses multiple areas of medicine. Offering numerous medical services allows him to fulfill his calling to help patients and their families achieve and sustain optimal health.</p>
  </div>

  <div class="feature feature-pi">
    <svg class="feature-icon" viewBox="0 0 46 46" fill="none" stroke="#111" stroke-width="1.6" aria-hidden="true">
      <path d="M2 2h22l7 7v12"/><path d="M24 2v7h7"/><path d="M2 2v40h20"/>
      <path d="M14 8v10M9 13h10"/><path d="M6 26h16M6 31h12M6 36h12"/>
      <path d="M35 22l10 4v8c0 6-5 9-10 11-5-2-10-5-10-11v-8z"/><path d="M30 33l4 4 6-7"/>
    </svg>
    <span class="feature-bar"></span>
    <div class="feature-text">Now accepting<br>PI cases on lien!</div>
  </div>

  <div class="feature feature-appt">
    <svg class="feature-icon" viewBox="0 0 46 46" fill="none" stroke="#111" stroke-width="1.6" aria-hidden="true">
      <rect x="2" y="5" width="36" height="33" rx="2"/><path d="M2 13h36"/>
      <path d="M8 2v6M15 2v6M22 2v6M29 2v6"/>
      <path d="M8 19h2M14 19h2M20 19h2M26 19h2M8 25h2M14 25h2M20 25h2M8 31h10"/>
      <circle cx="36" cy="35" r="9" fill="#fff"/><path d="M36 30v10M31 35h10"/>
    </svg>
    <span class="feature-bar"></span>
    <div class="feature-text">Same and next business day<br>appointments available for<br>initial visits, pre-operative clearances,<br>and all other medical needs</div>
  </div>

  <div class="feature feature-reports">
    <svg class="feature-icon" viewBox="0 0 46 46" fill="none" stroke="#111" stroke-width="1.6" aria-hidden="true">
      <path d="M2 2h30v24"/><path d="M2 2v42h24"/>
      <path d="M7 9h20M7 15h20M7 21h14M7 27h12"/><path d="M6 36l3 3 6-7"/>
      <circle cx="36" cy="35" r="9" fill="#fff"/><path d="M36 35l4-4"/><path d="M34 24h4M36 24v2"/>
    </svg>
    <span class="feature-bar"></span>
    <div class="feature-text">Expedited<br>medical reports<br>sent quickly to your office</div>
  </div>

  <div class="brand-name">WILLOWBROOK<br>MEDICAL CENTER</div>
  <div class="address">4150 Maple Ave., Fairview, CA, 90000</div>

  <div class="call-to-action">Call us for Appointment !</div>
  <div class="contact-line contact-phone"><span class="label">Ph : </span><span class="num">+(555) 410 - 2200</span></div>
  <div class="contact-line contact-fax"><span class="label">Fax : </span><span class="num">+(555) 410 - 2207</span></div>
</div>
</body>
</html>
```